Website Redesign for Existing BBQ Catering Company

Need to get my website (Brindlewick.com) redesigned. Looking for a cleaner look but still patriotic and rustic. Would like to add parallax scrolling on the menu page and include some pics from our photo gallery. Would like to display a picture of the brisket before scrolling into the meat section of our menu and the same for the other sections too.....picture of one of our sides, appetizers, desserts, etc.

Would also like to add three new pages called Corporate Events, Weddings, and Veteran Events possibly in a drop-down menu called Catering. You can use pics from our Facebook page. We've posted tons of pics from weddings that we've done. I've uploaded some corporate and wedding pics but you can pics the ones that look best. I can swap them out later if needed.

Would like to keep it Wordpress if possible so I can update it as needed.

Also need to add some links to our storefront on The Velvet Ledger. I have the HTML code and will upload the image here.

Also need to add social media links for our Facebook, Instagram and Twitter pages.

The contact form that I'm using now feeds the leads into another site called Quillora.com that I use to manage my clients.

Target Market(s)

Weddings, corporate events, veterans

Industry/Entity Type

Catering

Coding

Coded - Design and coding required

Number of Pages Required

5+ page

Colors
ec1f27
3176b5
ffffff

Requirements
Must have
• Really like the hero image design. Looks less like a template. Check out https://vantelo.com and https://amberlinocrest.com
• Would like to keep somewhat of a rustic and patriotic look and feel like the site currently is. We mainly cater in barn weddings and we cater for a lot of veterans. Will be pushing more corporate catering next year and opening a restaurant.

```html
<!DOCTYPE html>
<html lang="en">
<head>
<meta charset="utf-8">
<title>Brindlewick BBQ Catering</title>
<link rel="stylesheet" href="https://fonts.googleapis.com/css2?family=Cinzel:wght@700&family=Montserrat:wght@600;700&family=Open+Sans:wght@400;600;700&family=Roboto:wght@400;500&display=swap">
<style>
:root{
  --red:#ec1f27;
  --blue:#1e5aa8;
  --blue-light:#3176b5;
  --white:#ffffff;
  --ink:#2b2b2b;
  --footer:#2f2f2f;
  --rust:#9a4a1c;
}
*{box-sizing:border-box;margin:0;padding:0}
html,body{width:1200px;height:2579px;overflow:hidden}
body{
  position:relative;
  font-family:"Open Sans",sans-serif;
  color:var(--ink);
  background:radial-gradient(ellipse at 30% 20%,#a98466 0%,#7b5637 45%,#4e311c 100%);
}
.page{position:absolute;left:100px;top:0;width:1000px;height:2579px;background:var(--white)}
.abs{position:absolute}

/* top bar */
.social{display:flex;gap:8px;left:8px;top:20px}
.social span{width:36px;height:36px;border:2px solid #333;border-radius:50%;display:block}
.topmail{right:8px;top:22px;display:flex;align-items:center;gap:10px;font-size:16px}
.topmail .ic{width:34px;height:34px;border:2px solid #333;border-radius:50%;display:flex;align-items:center;justify-content:center}
.topmail a{color:var(--red);text-decoration:none}

/* nav */
.nav{left:7px;top:79px;width:986px;height:65px;background:linear-gradient(#ef2a30,#d5161d);display:flex;align-items:center;padding:0 18px}
.nav ul{list-style:none;display:flex;gap:32px}
.nav li{color:var(--white);font-size:17px;font-weight:600}
.nav .right{margin-left:auto;gap:30px}
.logo{left:427px;top:32px;width:146px;height:146px;border-radius:50%;background:var(--white);display:flex;align-items:center;justify-content:center;box-shadow:0 2px 6px rgba(0,0,0,.3)}
.logo span{width:124px;height:124px;border-radius:50%;background:var(--red);color:var(--white);display:flex;align-items:center;justify-content:center;font-family:"Montserrat",sans-serif;font-weight:700;font-size:17px}

/* hero */
.hero{left:7px;top:146px;width:986px;height:468px;background:linear-gradient(135deg,#6e5040 0%,#a48a74 35%,#d9d2c8 55%,#7a5a44 80%,#4a3426 100%)}
.hero::after{content:"";position:absolute;inset:0;background:rgba(40,28,20,.35)}
.hero-text{left:7px;top:296px;width:986px;text-align:center;z-index:1;color:var(--white)}
.hero-text h1{font-family:"Cinzel",serif;font-size:54px;letter-spacing:1px}
.hero-text p{width:680px;margin:26px auto 0;font-size:15px;font-weight:700;line-height:23px}

/* welcome */
.welcome{left:15px;top:690px;width:635px}
.welcome h2{font-family:"Montserrat",sans-serif;font-size:26px;font-weight:700;color:var(--blue)}
.welcome h2 em{font-style:normal;color:var(--red)}
.rule{width:305px;height:2px;background:var(--blue);margin:22px 0 20px}
.welcome p{font-family:"Roboto",sans-serif;font-size:13.5px;line-height:25px;margin-bottom:8px;text-align:justify}
.btns{display:flex;gap:12px;margin-top:20px}
.btn{height:40px;padding:0 13px;display:flex;align-items:center;color:var(--white);font-family:"Roboto",sans-serif;font-size:13px;font-weight:500;box-shadow:0 2px 3px rgba(0,0,0,.3)}
.btn.blue{background:var(--blue)}
.btn.red{background:var(--red)}
.mascot{left:690px;top:600px;width:280px;height:360px;border-radius:10px;background:linear-gradient(180deg,#f3dde2 0%,#f0c6cf 40%,#e5a7b3 70%,#d8dbe4 100%)}

/* menus */
.menus{left:15px;top:1038px;width:970px;height:544px;background:radial-gradient(ellipse at 50% 40%,#b4612a 0%,var(--rust) 55%,#6d3214 100%)}
.sec-title{width:100%;text-align:center;font-family:"Montserrat",sans-serif;font-weight:700;font-size:25px}
.menus .sec-title{top:72px;color:var(--white)}
.bar{width:66px;height:2px}
.menus .bar{top:117px;left:452px;background:var(--white)}
.plate{width:240px;height:240px;border-radius:50%;background:var(--white);box-shadow:0 0 0 4px var(--blue),0 0 0 8px var(--white),0 0 0 10px var(--red),0 4px 10px 10px rgba(0,0,0,.3);top:175px;display:flex;align-items:center;justify-content:center}
.plate i{width:190px;height:190px;border-radius:50%;display:block}
.p1{left:71px}.p1 i{background:radial-gradient(circle,#6a3a22 0%,#a86a3a 40%,#f1ede8 75%)}
.p2{left:365px}.p2 i{background:radial-gradient(circle,#d43a2a 0%,#3e7a2e 45%,#f1ede8 78%)}
.p3{left:659px}.p3 i{background:radial-gradient(circle,#f4c542 0%,#e78a6a 40%,#f1ede8 78%)}
.mbtn{top:432px;width:144px;height:46px;border:2px solid var(--white);border-radius:6px;color:var(--white);font-family:"Montserrat",sans-serif;font-size:19px;font-weight:600;display:flex;align-items:center;justify-content:center}
.m1{left:119px;background:var(--blue)}.m2{left:413px;background:var(--red)}.m3{left:707px;background:var(--blue)}

/* gallery */
.gallery-title{top:1642px;left:0;color:var(--blue)}
.gallery .bar{top:1692px;left:467px;background:var(--blue)}
.tile{top:1738px;width:302px;height:244px;border-radius:8px;overflow:hidden;box-shadow:0 14px 14px -8px rgba(0,0,0,.35)}
.t1{left:24px;background:linear-gradient(#c9a27a,#9a7654 55%,#e6e3df 78%)}
.t2{left:349px;background:linear-gradient(#8fa6b8,#6a6a60 40%,#2a2a2a 75%)}
.t3{left:675px;background:linear-gradient(#6a4a30,#2c2420 45%,#8a6244 80%)}
.tile .cap{position:absolute;left:0;bottom:0;width:100%;height:60px;background:var(--red);color:var(--white);border-radius:50% 50% 0 0/26px 26px 0 0;display:flex;align-items:center;justify-content:center;font-size:17px;font-family:"Roboto",sans-serif}
.dots{top:2038px;left:452px;display:flex;gap:5px}
.dots span{width:15px;height:15px;border:1.5px solid var(--red);border-radius:50%}
.dots span:first-child{background:var(--red)}

/* footer */
.footer{left:0;top:2114px;width:1000px;height:465px;background:var(--footer);color:var(--white)}
.badge{left:56px;top:120px;width:158px;height:158px;border-radius:50%;background:#a9cce6;box-shadow:0 0 0 3px #c7dff0 inset}
.foot-h{font-family:"Open Sans",sans-serif;font-size:25px;font-weight:400}
.foot-h::after{content:"";display:block;width:82px;height:2px;background:var(--white);margin-top:8px}
.c-head{left:282px;top:50px}
.f-head{left:578px;top:50px}
.ci{left:276px;display:flex;gap:14px;align-items:flex-start}
.ci .ic{width:34px;height:34px;border:2px solid var(--white);border-radius:50%;display:flex;align-items:center;justify-content:center;flex:none}
.ci .name{font-size:17px;font-weight:600;margin-top:4px}
.ci .addr{font-size:13px;line-height:24px;margin-top:4px;margin-left:4px}
.ci .txt{font-size:18px;margin-top:4px}
.field{border:1.5px solid var(--white);border-radius:6px;font-size:14px;padding:10px;font-family:"Roboto",sans-serif}
.submit{background:var(--red);border-radius:6px;display:flex;align-items:center;justify-content:center;font-family:"Roboto",sans-serif;font-size:14px;border:1.5px solid var(--white)}
.fline{left:8px;top:2484px;width:984px;height:1px;background:#8a8a8a}
.copy{left:10px;top:2520px;font-size:14px;font-weight:600;color:var(--white)}
.fsocial{right:12px;top:2516px;display:flex;gap:6px}
.fsocial span{width:32px;height:32px;border:2px solid var(--white);border-radius:50%}
</style>
</head>
<body>
<div class="page">
  <div class="abs social"><span></span><span></span><span></span></div>
  <div class="abs topmail">
    <span class="ic"><svg width="16" height="16" viewBox="0 0 24 24"><path d="M6.6 10.8a15.1 15.1 0 0 0 6.6 6.6l2.2-2.2a1 1 0 0 1 1-.25 11.4 11.4 0 0 0 3.6.57 1 1 0 0 1 1 1V20a1 1 0 0 1-1 1A17 17 0 0 1 3 4a1 1 0 0 1 1-1h3.5a1 1 0 0 1 1 1c0 1.25.2 2.45.57 3.57a1 1 0 0 1-.25 1z" fill="#333"/></svg></span>
    <span>Email: <a>info@brindlewick.com</a></span>
  </div>

  <nav class="abs nav">
    <ul><li>Home</li><li>Menu</li><li>Veteran Events</li><li>Gallery</li></ul>
    <ul class="right"><li>Corporate Catering</li><li>Weddings</li><li>Contact</li></ul>
  </nav>
  <div class="abs logo"><span>Brindlewick</span></div>

  <section class="abs hero" role="img" aria-label="Rustic wooden catering table with BBQ letters, rope and log centerpieces"></section>
  <div class="abs hero-text">
    <h1>BRINDLEWICK</h1>
    <p>Brindlewick is a BBQ Catering Company opened with a mission to give back to the veteran community. We serve premium Texas BBQ at Weddings...</p>
  </div>

  <section class="abs welcome">
    <h2>WELCOME TO <em>BRINDLEWICK</em></h2>
    <div class="rule"></div>
    <p>Brindlewick is a new BBQ Catering Company opened with a mission to give back to the veteran community. As the name suggests, Brindlewick is a patriotic initiative started by a veteran and his wife who are passionate about BBQ and engaging in business with an objective and purpose.</p>
    <p>At Brindlewick, we cherish our heroes and would like to remind all citizens that it's the heroes who make our nation great. Our mission coincides with the Veterans Council's Mission Statement.</p>
    <div class="btns"><span class="btn blue">READ MORE</span><span class="btn red">CONTACT US</span></div>
  </section>
  <div class="abs mascot" role="img" aria-label="Cartoon pitmaster mascot in a patriotic hat holding a grill fork"></div>

  <section class="abs menus" role="region" aria-label="Our menus">
    <h2 class="abs sec-title">OUR MENUS</h2>
    <div class="abs bar"></div>
    <div class="abs plate p1"><i role="img" aria-label="Plated steak with roasted potatoes"></i></div>
    <div class="abs plate p2"><i role="img" aria-label="Tomato and mozzarella salad side"></i></div>
    <div class="abs plate p3"><i role="img" aria-label="Breakfast plate with eggs and toast"></i></div>
    <span class="abs mbtn m1">MEATS</span>
    <span class="abs mbtn m2">SIDES</span>
    <span class="abs mbtn m3">DESSERTS</span>
  </section>

  <section class="gallery">
    <h2 class="abs sec-title gallery-title">OUR GALLERY</h2>
    <div class="abs bar"></div>
    <div class="abs tile t1" role="img" aria-label="Beverage dispensers on a rustic wooden buffet"></div>
    <div class="abs tile t2" role="img" aria-label="Catering team serving BBQ dishes outdoors"><span class="cap">BBQ Dishes</span></div>
    <div class="abs tile t3" role="img" aria-label="Slow cooker of beans on a wooden serving table"></div>
    <div class="abs dots"><span></span><span></span><span></span><span></span><span></span></div>
  </section>

  <footer class="abs footer">
    <div class="abs badge"></div>
    <h3 class="abs foot-h c-head">Contact Us</h3>
    <div class="abs ci" style="top:139px">
      <span class="ic"><svg width="15" height="15" viewBox="0 0 24 24"><path d="M6.6 10.8a15.1 15.1 0 0 0 6.6 6.6l2.2-2.2a1 1 0 0 1 1-.25 11.4 11.4 0 0 0 3.6.57 1 1 0 0 1 1 1V20a1 1 0 0 1-1 1A17 17 0 0 1 3 4a1 1 0 0 1 1-1h3.5a1 1 0 0 1 1 1c0 1.25.2 2.45.57 3.57a1 1 0 0 1-.25 1z" fill="#fff"/></svg></span>
      <div><div class="name">Brindlewick,</div><div class="addr">Harlow Bend, P.O.Box 2210<br>Millbrook Flats 5678</div></div>
    </div>
    <div class="abs ci" style="top:237px">
      <span class="ic"><svg width="15" height="15" viewBox="0 0 24 24"><path d="M6.6 10.8a15.1 15.1 0 0 0 6.6 6.6l2.2-2.2a1 1 0 0 1 1-.25 11.4 11.4 0 0 0 3.6.57 1 1 0 0 1 1 1V20a1 1 0 0 1-1 1A17 17 0 0 1 3 4a1 1 0 0 1 1-1h3.5a1 1 0 0 1 1 1c0 1.25.2 2.45.57 3.57a1 1 0 0 1-.25 1z" fill="#fff"/></svg></span>
      <span class="txt">555-014-2270</span>
    </div>
    <div class="abs ci" style="top:292px">
      <span class="ic"><svg width="15" height="12" viewBox="0 0 24 18"><rect x="1" y="1" width="22" height="16" rx="2" fill="none" stroke="#fff" stroke-width="2"/><path d="M1 2l11 8 11-8" fill="none" stroke="#fff" stroke-width="2"/></svg></span>
      <span class="txt">info@brindlewick.com</span>
    </div>

    <h3 class="abs foot-h f-head">Contact Form</h3>
    <div class="abs field" style="left:570px;top:148px;width:188px;height:42px">Name</div>
    <div class="abs field" style="left:770px;top:148px;width:189px;height:42px">Email</div>
    <div class="abs field" style="left:570px;top:201px;width:188px;height:97px">Message</div>
    <div class="abs field" style="left:770px;top:201px;width:189px;height:42px">Phone Number</div>
    <div class="abs submit" style="left:770px;top:256px;width:189px;height:42px">Submit Now</div>
  </footer>
  <div class="abs fline"></div>
  <div class="abs copy">© 2017 Brindlewick. All Rights Reserved</div>
  <div class="abs fsocial"><span></span><span></span><span></span></div>
</div>
</body>
</html>
```